Business Card Design Project

Business card design based on the existing logo.

Target Market(s)

Small to medium business owners and CIO's looking for professional IT services.

Industry/Entity Type

Business

Font styles to use
Serif
Sans Serif

Requirements
Must have
• Logo, company name, company details

Text to appear on the business card
Name / Title:
Leon Fairholt
CEO

Address:
Valtiro Limited
Level 3, 42 Kestle St
P O Box 462
Paraparaumu 5391

Other details:
leon@valtiro.co
Ph: 0800 519 308
Mob: +64 21 948 216
www.valtiro.co

Nice to have
• I would look at both single and double sided options. My initial thought is double sided with just the logo with the grey framing for the front and the name and details on the back. But I'm open to other design options.

```html
<!DOCTYPE html>
<html lang="en">
<head>
<meta charset="utf-8">
<title>Valtiro Limited – Business Card</title>
<link rel="stylesheet" href="https://fonts.googleapis.com/css2?family=Source+Sans+3:wght@400;600;700&display=swap">
<style>
  :root {
    --teal: #1b5f7d;
    --teal-dark: #174f69;
    --white: #ffffff;
    --ink: #1e1e1e;
    --grey: #8a8f93;
    --rule: #20282c;
    --backdrop: #e9eaeb;
  }
  * { box-sizing: border-box; margin: 0; padding: 0; }
  html, body {
    width: 1200px; height: 720px; overflow: hidden;
    background: var(--backdrop);
    font-family: "Source Sans 3", Arial, sans-serif;
  }
  .canvas { position: relative; width: 1200px; height: 720px; }
  .card {
    position: absolute; top: 205px;
    width: 530px; height: 303px;
    overflow: hidden;
    box-shadow: 0 6px 18px rgba(0,0,0,.18);
  }
  .card--details { left: 50px; background: var(--white); }
  .card--brand { left: 620px; background: var(--teal); }

  .wordmark {
    display: flex; align-items: center; justify-content: center; gap: 14px;
    font-weight: 600; letter-spacing: .5px;
  }
  .wordmark__dot { border-radius: 50%; flex: none; }
  .card--details .wordmark {
    position: absolute; top: 38px; left: 0; right: 0;
    font-size: 58px; color: var(--ink);
  }
  .card--details .wordmark__dot { width: 34px; height: 34px; background: var(--teal); }
  .card--brand .wordmark {
    position: absolute; top: 50%; left: 0; right: 0; transform: translateY(-50%);
    font-size: 64px; color: var(--white);
  }
  .card--brand .wordmark__dot { width: 38px; height: 38px; background: var(--white); }

  .holder {
    position: absolute; top: 132px; left: 0; right: 0; text-align: center;
    color: var(--teal); font-weight: 700; font-size: 17px;
  }
  .holder__title { color: var(--grey); font-weight: 400; font-size: 12px; }

  .contact-band {
    position: absolute; left: 0; right: 0; bottom: 0; height: 122px;
    background: var(--teal);
    border-top: 3px solid var(--rule);
  }
  .contact-band::before {
    content: ""; position: absolute; left: 0; right: 0; top: -9px; height: 3px;
    background: var(--rule);
  }
  .address, .channels {
    position: absolute; top: 16px;
    color: var(--white); font-size: 14px; line-height: 20px;
  }
  .address { right: 275px; text-align: right; }
  .divider {
    position: absolute; top: 16px; left: 262px; width: 1px; height: 80px;
    background: rgba(255,255,255,.75);
  }
  .channels { left: 276px; list-style: none; }
  .channels li { display: flex; align-items: center; gap: 8px; }
  .channels svg { width: 12px; height: 12px; flex: none; }
</style>
</head>
<body>
<main class="canvas">

  <section class="card card--details" aria-label="Business card, details side">
    <div class="wordmark"><span class="wordmark__dot"></span>Valtiro</div>
    <p class="holder">Leon Fairholt, <span class="holder__title">CEO</span></p>

    <div class="contact-band">
      <address class="address">
        Valtiro Limited<br>
        Level 3, 42 Kestle St<br>
        P O Box 462<br>
        Paraparaumu 5391
      </address>
      <span class="divider"></span>
      <ul class="channels">
        <li>
          <svg viewBox="0 0 12 12" aria-hidden="true"><circle cx="6" cy="6" r="5.5" fill="#fff"/><path d="M4 3.2l1 1.4-.6.7c.4.9 1 1.6 1.9 2l.7-.6 1.4 1-.6 1.1C5.6 8.6 3.4 6.4 3.2 4z" fill="var(--teal)"/></svg>
          0800 519 308
        </li>
        <li>
          <svg viewBox="0 0 12 12" aria-hidden="true"><rect x="3" y="1" width="6" height="10" rx="1" fill="#fff"/><rect x="4" y="2.3" width="4" height="5.5" fill="var(--teal)"/></svg>
          +64 21 948 216
        </li>
        <li>
          <svg viewBox="0 0 12 12" aria-hidden="true"><circle cx="6" cy="6" r="5.5" fill="#fff"/><rect x="3" y="4" width="6" height="4.2" fill="var(--teal)"/><path d="M3 4l3 2.3L9 4" stroke="#fff" stroke-width=".7" fill="none"/></svg>
          leon@valtiro.co
        </li>
        <li>
          <svg viewBox="0 0 12 12" aria-hidden="true"><circle cx="6" cy="6" r="5.5" fill="#fff"/><circle cx="6" cy="6" r="3.4" fill="none" stroke="var(--teal)" stroke-width=".8"/><path d="M2.6 6h6.8M6 2.6c-1.6 2-1.6 4.8 0 6.8M6 2.6c1.6 2 1.6 4.8 0 6.8" stroke="var(--teal)" stroke-width=".7" fill="none"/></svg>
          www.valtiro.co
        </li>
      </ul>
    </div>
  </section>

  <section class="card card--brand" aria-label="Business card, brand side">
    <div class="wordmark"><span class="wordmark__dot"></span>Valtiro</div>
  </section>

</main>
</body>
</html>
```